Small and passionate motorcycle workshop requires a business card that kicks butt!

I'm Dermot, I'm passionate about my motorcycles, I'm passionate about my desert racing and I'm a passionate motorcycle technician, that's why I started my own motorcycle workshop: 'Rivo Tarka'.
I started my workshop in my dining room and it’s eventually moved into a newly renovated shed that my Grandpa built with his own two hands in the early 1960's. To the customer the shed looks like a farm shed on my property, however the inside is ready for open heart surgery on their "Baby" which could be a late model sports bike, a highway cruiser, an old four-wheeler or an off road desert racing weapon!
This business is my own, I've built it from my dining room floor and I'm deeply passionate about it.
I need a professional business card and logo which looks like a heart and soul is intermingled through it because that is how my business is run. Rivo Tarka may have started from my dining room but it has always been professionally run and I have always put my passion into the bikes I've worked on.

-The text only logo needs to be comprised of 'Rivo Tarka'
-The business card will be double sided

And I do realise it will be a hard task to make something look professional and personal at the same time...however there are some very talented people in this world and I can’t wait to see what you create!

I've added some logo/designs that I'm fond of.

Industry/Entity Type

Racing

Requirements
Must have
• My name - Dermot Fasquell
My Qualification - Qualified Motorcycle Technician
Ph - 0487305219
Email - rivotarka@kelpmail.example
Address - 17 Bellwin Ridge Road, Williamstown, SA
ABN - 62 918 304 217 (plesase include the 'ABN' part
Needs to include these dot points:
-Servicing
-Repairs
-All makes/models
-Weekends by appt.
-Pick-up/delivery available
Nice to have
• I like the idea of calling myself a "Qualified and Passionate Motorcycle Technician". If the card does not come across that it’s a passionate business I'd like this line to be used on the card near my name.

One idea I like would include having the text only logo on the front being quite bold and contrasted to the background, then having my name and number smaller underneath somewhere. I'm very open to whatever comes my way so I'm look forward to seeing some sweet ideas!

```html
<!DOCTYPE html>
<html lang="en">
<head>
<meta charset="utf-8">
<title>Rivo Tarka – Business Card</title>
<link href="https://fonts.googleapis.com/css2?family=Comfortaa:wght@400;600;700&display=swap" rel="stylesheet">
<style>
  :root {
    --charcoal: #3f3f3f;
    --frame-grey: #777777;
    --white: #ffffff;
    --stripe-orange: #d98a2e;
    --sand: #e8b57f;
    --mark-dark: #404040;
  }
  html, body {
    margin: 0;
    padding: 0;
    overflow: hidden;
    background: #ffffff;
  }
  .card {
    position: relative;
    width: 1200px;
    height: 963px;
    overflow: hidden;
    font-family: 'Comfortaa', sans-serif;
    color: var(--white);
  }
  .side-front {
    position: absolute;
    left: 0; top: 0;
    width: 595px; height: 963px;
    background: var(--charcoal);
  }
  .side-back {
    position: absolute;
    left: 595px; top: 0;
    width: 605px; height: 963px;
    background: var(--stripe-orange);
  }
  .side-back .sand-band {
    position: absolute;
    left: 56px; top: 0;
    width: 506px; height: 963px;
    background: var(--sand);
  }
  .logo-box {
    position: absolute;
    left: 117px; top: 18px;
    width: 360px; height: 323px;
    background: var(--frame-grey);
    display: flex;
    align-items: center;
    justify-content: center;
  }
  .logo-box .wordmark {
    font-size: 44px;
    font-weight: 700;
    color: var(--white);
    letter-spacing: 1px;
  }
  .owner-name {
    position: absolute;
    left: 0; top: 360px;
    width: 595px;
    margin: 0;
    text-align: center;
    font-size: 46px;
    font-weight: 600;
    letter-spacing: 1px;
  }
  .tagline {
    position: absolute;
    left: 0; top: 418px;
    width: 595px;
    margin: 0;
    text-align: center;
    font-size: 22px;
    line-height: 30px;
    letter-spacing: 1px;
  }
  .service {
    position: absolute;
    display: flex;
    align-items: flex-start;
    gap: 10px;
    font-size: 24px;
    line-height: 29px;
  }
  .service svg, .contact svg {
    flex: none;
    fill: var(--white);
  }
  .service-servicing { left: 54px; top: 510px; }
  .service-repairs { left: 54px; top: 558px; }
  .service-pickup { left: 54px; top: 606px; }
  .service-models { left: 318px; top: 510px; }
  .service-weekends { left: 318px; top: 558px; }
  .contact {
    position: absolute;
    left: 54px;
    display: flex;
    align-items: flex-start;
    gap: 24px;
    font-size: 24px;
    line-height: 32px;
    letter-spacing: 1px;
  }
  .contact-address { top: 688px; }
  .contact-phone { top: 762px; }
  .contact-email { top: 818px; }
  .contact-abn { top: 872px; }
  .back-mark {
    position: absolute;
    left: 250px; top: 200px;
    width: 120px; height: 470px;
    display: flex;
    align-items: center;
    justify-content: center;
  }
  .back-mark .wordmark {
    writing-mode: vertical-rl;
    font-size: 86px;
    font-weight: 700;
    color: var(--mark-dark);
    letter-spacing: 2px;
    white-space: nowrap;
  }
</style>
</head>
<body>
<div class="card">
  <section class="side-front">
    <div class="logo-box">
      <span class="wordmark">Rivo Tarka</span>
    </div>

    <h1 class="owner-name">Dermot Fasquell</h1>
    <p class="tagline">Qualified and Passionate<br>Motorcycle Technician</p>

    <div class="service service-servicing">
      <svg width="32" height="32" viewBox="0 0 34 34" aria-hidden="true">
        <circle cx="17" cy="17" r="13" fill="none" stroke="#fff" stroke-width="6" stroke-dasharray="4 3.5"/>
        <circle cx="17" cy="17" r="10"/>
        <circle cx="17" cy="17" r="4" fill="#3f3f3f"/>
      </svg>
      <span>Servicing</span>
    </div>
    <div class="service service-repairs">
      <svg width="32" height="32" viewBox="0 0 34 34" aria-hidden="true">
        <path d="M30 6a8 8 0 0 1-10 9L7 28a3 3 0 0 1-4-4L16 11a8 8 0 0 1 9-10l-5 5 2 5 5 2z"/>
      </svg>
      <span>Repairs</span>
    </div>
    <div class="service service-pickup">
      <svg width="32" height="32" viewBox="0 0 34 34" aria-hidden="true">
        <path d="M2 8h18v16H2zM21 13h6l5 6v5H21z"/>
        <circle cx="8" cy="26" r="4" stroke="#3f3f3f" stroke-width="2"/>
        <circle cx="26" cy="26" r="4" stroke="#3f3f3f" stroke-width="2"/>
      </svg>
      <span>Pick-up/delivery<br>available</span>
    </div>
    <div class="service service-models">
      <svg width="34" height="34" viewBox="0 0 36 36" aria-hidden="true">
        <circle cx="18" cy="18" r="15" fill="none" stroke="#fff" stroke-width="3"/>
        <rect x="16.5" y="7" width="3" height="14" rx="1.5"/>
        <circle cx="18" cy="22" r="3.5"/>
      </svg>
      <span>All makes/models</span>
    </div>
    <div class="service service-weekends">
      <svg width="32" height="34" viewBox="0 0 34 36" aria-hidden="true">
        <rect x="3" y="5" width="28" height="28" rx="2" fill="none" stroke="#fff" stroke-width="3"/>
        <rect x="3" y="5" width="28" height="6"/>
        <rect x="8" y="1" width="3" height="7"/>
        <rect x="23" y="1" width="3" height="7"/>
        <rect x="8" y="15" width="18" height="13" fill="none" stroke="#fff" stroke-width="2"/>
      </svg>
      <span>Weekends<br>by appt.</span>
    </div>

    <div class="contact contact-address">
      <svg width="36" height="36" viewBox="0 0 36 36" aria-hidden="true">
        <path d="M18 3 2 18h5v15h8V23h6v10h8V18h5z"/>
      </svg>
      <span>17 Bellwin Ridge Road,<br>Williamstown, SA</span>
    </div>
    <div class="contact contact-phone">
      <svg width="36" height="36" viewBox="0 0 36 36" aria-hidden="true">
        <path d="M9 3l6 8-3 4c2 4 5 7 9 9l4-3 8 6-4 6C16 33 3 20 3 7z"/>
      </svg>
      <span>0487 305219</span>
    </div>
    <div class="contact contact-email">
      <svg width="38" height="32" viewBox="0 0 38 32" aria-hidden="true">
        <path d="M2 14 19 2l17 12v16H2z" fill="none" stroke="#fff" stroke-width="2.5"/>
        <path d="M2 14l17 10 17-10" fill="none" stroke="#fff" stroke-width="2.5"/>
      </svg>
      <span>rivotarka@kelpmail.example</span>
    </div>
    <div class="contact contact-abn">
      <svg width="36" height="36" viewBox="0 0 36 36" aria-hidden="true">
        <path d="M4 18 18 4h13v13L17 31z"/>
        <circle cx="25" cy="11" r="3" fill="#3f3f3f"/>
      </svg>
      <span>ABN - 62 918 304 217</span>
    </div>
  </section>

  <section class="side-back">
    <div class="sand-band"></div>
    <div class="back-mark">
      <span class="wordmark">Rivo Tarka</span>
    </div>
  </section>
</div>
</body>
</html>
```